Presentation Folder Design for Photographer

Professional photographer requires a presentation folder for marketing.
I specialise in architecture, corporate & commercial photography. The folder will be used to promote my architectural photography services to real estate, accomodation & architect clients.

I'm looking for a modern clean design that complements my logo with complimentary text & colours. I want to use some images in the design, probably a mix of images not just architectural. I need a print ready design in PDF as well as a PSD file that I can possibly edit / update images later on.

The folder will be a double sided design with no need for pockets included in the design. Overall dimensions are 430mm ( folded down the centre ) x 315mm with a 5mm trim & bleed.

The layout would be as follows :

Front cover - Logo + maybe some images or some other design work.

Inside front cover - Some text about my services.

ARCHITECTURE
Commercial Residential Real Estate Drone Floorpans Accommodation

CORPORATE
Studio Headshots Environmental Portraits Staff Photography

COMMERCIAL
Product Advertising Fashion Event Stock

Inside back cover - no text as a seperate price list will sit here.

Outside back cover - I was thinking of having a collage of images worked into
the design but open to the designers input as well.
I also have another logo with phone number & web address
I would like on the back cover - Will be included in the files
provided.

I have a black background & white background version of my logo I will include both for the design work. I'm trying to get away from an all black design so if using the black logo I don't want a completely black page design, just becomes to heavy.

I'm redoing my website soon so please base the folder design around my logo text & colours not my current website as it's very outdated.

Logo brand guide is as follows

Main Font Font: Reislust
Main Font Color: #fff
Slogan Font Font: Ubuntu Bold
Monogram Font Font: Venti Medium
Container Color: #fff

Please respect the copyright on the images provided and delete all content once the design has been completed.
Thanks.

Need extra days to review

```html
<!DOCTYPE html>
<html lang="en">
<head>
<meta charset="utf-8">
<title>Lens Harbour – Presentation Folder</title>
<link href="https://fonts.googleapis.com/css2?family=Josefin+Sans:wght@300&family=Lato:wght@400;700&display=swap" rel="stylesheet">
<style>
  :root {
    --stage: #5f5f5f;
    --ink: #0b0b0b;
    --ink-soft: #1a1a1a;
    --gold: #c79c52;
    --gold-panel: #b5884a;
    --gold-deep: #9c733a;
    --white: #ffffff;
  }
  * { box-sizing: border-box; margin: 0; padding: 0; }
  html, body { width: 960px; height: 1200px; overflow: hidden; background: var(--stage); }
  .canvas { position: relative; width: 960px; height: 1200px; }

  .spread { position: absolute; left: 90px; width: 780px; height: 571px; display: flex; }
  .spread--outside { top: 20px; }
  .spread--inside { top: 609px; }
  .panel { position: relative; width: 390px; height: 571px; overflow: hidden; }
  .panel > svg { position: absolute; inset: 0; }

  /* brand lockup */
  .brand { position: absolute; display: flex; align-items: center; gap: 8px; }
  .brand__mark { width: 22px; height: 22px; border: 2px solid var(--gold); }
  .brand__name {
    font-family: "Josefin Sans", sans-serif; font-weight: 300;
    font-size: 15px; letter-spacing: 3px; color: var(--gold); line-height: 1;
  }
  .brand__tagline {
    font-family: "Lato", sans-serif; font-weight: 700;
    font-size: 5px; letter-spacing: 1.6px; color: var(--gold);
    text-transform: uppercase; margin-top: 3px;
  }

  /* front cover */
  .cover-front { background: var(--ink); }
  .cover-front .brand { top: 48px; left: 50%; transform: translateX(-50%); }
  .cover-front__url {
    position: absolute; bottom: 36px; width: 100%; text-align: center;
    font-family: "Lato", sans-serif; font-weight: 700; font-size: 12px;
    letter-spacing: 2.4px; color: var(--gold);
  }

  /* back cover */
  .cover-back { background: var(--ink); }
  .cover-back .brand { left: 130px; top: 400px; }
  .contact {
    position: absolute; list-style: none;
    font-family: "Lato", sans-serif; font-size: 10px; color: var(--gold);
  }
  .contact li { display: flex; align-items: center; gap: 8px; margin-bottom: 7px; }
  .contact svg { width: 11px; height: 11px; flex: none; }
  .contact--studio { left: 34px; bottom: 34px; }
  .contact--online { left: 220px; bottom: 100px; }

  /* inside */
  .inside-left { background: var(--ink); }
  .inside-left .brand { top: 120px; left: 50%; transform: translateX(-50%); }
  .inside-right { background: var(--gold-panel); }
  .inside-right .brand { top: 200px; left: 50%; transform: translateX(-50%); }
  .inside-right .brand__mark { border-color: #e2b86a; }
  .inside-right .brand__name, .inside-right .brand__tagline { color: #e2b86a; }
</style>
</head>
<body>
<main class="canvas">

  <!-- Outside spread: back cover + front cover -->
  <section class="spread spread--outside">

    <article class="panel cover-back">
      <svg width="390" height="571" viewBox="0 0 390 571">
        <defs>
          <linearGradient id="nightScene" x1="0" y1="0" x2="0" y2="1">
            <stop offset="0" stop-color="#2b2b2b"/>
            <stop offset="0.55" stop-color="#141414"/>
            <stop offset="1" stop-color="#0b0b0b"/>
          </linearGradient>
        </defs>
        <rect width="390" height="571" fill="url(#nightScene)" role="img" aria-label="Night photograph of a heritage building, faded into black"/>
        <g class="collage">
          <path d="M20 290 L20 140 A150 150 0 0 1 124 166 Z" fill="#a3271f" role="img" aria-label="Photo of a stage performer in red"/>
          <path d="M20 290 L124 166 A150 150 0 0 1 166 326 Z" fill="#5a4a48" role="img" aria-label="Photo of a businessman beside a red sports car"/>
          <path d="M20 290 L166 326 A150 150 0 0 1 20 440 Z" fill="#2d5fb5" role="img" aria-label="Photo of a classic blue car outside a shop"/>
          <path d="M20 290 L20 440 A150 150 0 0 1 0 438 L0 142 A150 150 0 0 1 20 140 Z" fill="#3a3030"/>
          <circle cx="20" cy="290" r="150" fill="none" stroke="var(--white)" stroke-width="2.5"/>
          <line x1="20" y1="290" x2="124" y2="166" stroke="var(--white)" stroke-width="1.5"/>
          <line x1="20" y1="290" x2="166" y2="326" stroke="var(--white)" stroke-width="1.5"/>
          <circle cx="20" cy="290" r="70" fill="#6e5f58" stroke="var(--white)" stroke-width="2" role="img" aria-label="Silver-painted fashion portrait"/>
        </g>
      </svg>

      <div class="brand">
        <span class="brand__mark"></span>
        <div><div class="brand__name">LENS HARBOUR</div><div class="brand__tagline">Architecture Corporate Commercial</div></div>
      </div>

      <ul class="contact contact--online">
        <li><svg viewBox="0 0 12 12"><rect x="1" y="3" width="10" height="7" fill="none" stroke="currentColor"/><path d="M1 3 L6 7 L11 3" fill="none" stroke="currentColor"/></svg>hello@lensharbour.com.au</li>
        <li><svg viewBox="0 0 12 12"><circle cx="6" cy="6" r="5" fill="none" stroke="currentColor"/><path d="M1 6 H11 M6 1 C3 4 3 8 6 11 M6 1 C9 4 9 8 6 11" fill="none" stroke="currentColor"/></svg>www.lensharbour.com.au</li>
      </ul>
      <ul class="contact contact--studio">
        <li><svg viewBox="0 0 12 12"><path d="M3 1 L5 3.5 L4 5 C5 7 6 8 7 8 L8.5 7 L11 9 L9.5 11 C5 11 1 7 1 2.5 Z" fill="currentColor"/></svg>0412 555 018</li>
        <li><svg viewBox="0 0 12 12"><path d="M6 11 C3 7 2 5.5 2 4.5 A4 4 0 0 1 10 4.5 C10 5.5 9 7 6 11 Z" fill="currentColor"/><circle cx="6" cy="4.5" r="1.4" fill="var(--ink)"/></svg>12 Ridge Rd Elmsford, VIC, 3999</li>
      </ul>
    </article>

    <article class="panel cover-front">
      <svg width="390" height="571" viewBox="0 0 390 571">
        <g class="frame-corners" fill="none" stroke="var(--gold)" stroke-width="3">
          <polyline points="40,160 40,110 90,110"/>
          <polyline points="300,110 350,110 350,160"/>
          <polyline points="40,400 40,450 90,450"/>
          <polyline points="300,450 350,450 350,400"/>
        </g>
        <g class="collage">
          <path d="M195 280 L143.7 139 A150 150 0 0 1 336 228.7 Z" fill="#d9c3a4" role="img" aria-label="Photo of a styled guest bedroom"/>
          <path d="M195 280 L336 228.7 A150 150 0 0 1 291.4 394.9 Z" fill="#e8dccb" role="img" aria-label="Photo of a white living room with framed art"/>
          <path d="M195 280 L291.4 394.9 A150 150 0 0 1 120 409.9 Z" fill="#c9b590" role="img" aria-label="Photo of a modern kitchen"/>
          <path d="M195 280 L120 409.9 A150 150 0 0 1 47.3 253.9 Z" fill="#cfb79a" role="img" aria-label="Photo of a bedroom with lamps"/>
          <path d="M195 280 L47.3 253.9 A150 150 0 0 1 143.7 139 Z" fill="#bfa88a" role="img" aria-label="Photo of a bedroom interior"/>
          <g stroke="var(--white)" stroke-width="1.5">
            <line x1="195" y1="280" x2="143.7" y2="139"/>
            <line x1="195" y1="280" x2="336" y2="228.7"/>
            <line x1="195" y1="280" x2="291.4" y2="394.9"/>
            <line x1="195" y1="280" x2="120" y2="409.9"/>
            <line x1="195" y1="280" x2="47.3" y2="253.9"/>
          </g>
          <circle cx="195" cy="280" r="150" fill="none" stroke="var(--white)" stroke-width="3"/>
          <circle cx="195" cy="280" r="72" fill="#2a2522" stroke="var(--white)" stroke-width="2" role="img" aria-label="Studio portrait of a woman"/>
        </g>
      </svg>

      <div class="brand">
        <span class="brand__mark"></span>
        <div><div class="brand__name">LENS HARBOUR</div><div class="brand__tagline">Architecture Corporate Commercial</div></div>
      </div>
      <p class="cover-front__url">www.lensharbour.com.au</p>
    </article>
  </section>

  <!-- Inside spread -->
  <section class="spread spread--inside">
    <article class="panel inside-left">
      <svg width="390" height="571" viewBox="0 0 390 571">
        <defs>
          <linearGradient id="foldSheen" x1="0" y1="0" x2="1" y2="0">
            <stop offset="0" stop-color="#0b0b0b"/>
            <stop offset="0.7" stop-color="#1e1e1e"/>
            <stop offset="0.9" stop-color="#3a3a3a"/>
            <stop offset="1" stop-color="#111"/>
          </linearGradient>
        </defs>
        <rect width="390" height="571" fill="url(#foldSheen)"/>
      </svg>
      <div class="brand">
        <span class="brand__mark"></span>
        <div><div class="brand__name">LENS HARBOUR</div><div class="brand__tagline">Architecture Corporate Commercial</div></div>
      </div>
    </article>

    <article class="panel inside-right">
      <div class="brand">
        <span class="brand__mark"></span>
        <div><div class="brand__name">LENS HARBOUR</div><div class="brand__tagline">Architecture Corporate Commercial</div></div>
      </div>
      <svg width="390" height="571" viewBox="0 0 390 571">
        <path d="M0 571 L0 430 C0 385 50 355 120 355 C190 355 230 400 260 470 L300 571 Z" fill="var(--ink)"/>
      </svg>
    </article>
  </section>

</main>
</body>
</html>
```